RevelHubQZ Business Cards

Front
Has logo with a design. Website address (www.revelhubqz.example)
Has slogan (discover nightlife)
Has phone number (5129873304)
Should be bold and stands out.

Back
Has details about what we offer.

Events
Search upcoming events
Submit events
Party Image Gallery
View and download HQ party images
Sign up as a contributing event photographer and get paid!
Tickets
Sell your event tickets online for free!
Direct pay
No ticket fee

Target Market(s)

These cards will be handed out in clubs and events to patrons.

Industry/Entity Type

Business

Contact Information for Business Card

Should match or mirror our website in some sort of way. Visit the website to get ideas.

Requirements
Must have
• Must be designed for a 3x3 inch card.

```html
<!DOCTYPE html>
<html lang="en">
<head>
<meta charset="utf-8">
<title>RevelHubQZ Business Cards</title>
<link rel="stylesheet" href="https://fonts.googleapis.com/css2?family=Questrial&display=swap">
<style>
  :root {
    --stage: #2b2b2b;
    --card: #050505;
    --card-soft: #141414;
    --blue: #35a8e0;
    --pink: #e8439a;
    --text: #e6e6e6;
    --muted: #b5b5b5;
  }
  * { box-sizing: border-box; margin: 0; padding: 0; }
  html, body { width: 1200px; height: 800px; overflow: hidden; }
  body {
    background: var(--stage);
    font-family: "Questrial", "Century Gothic", sans-serif;
    display: flex; align-items: center; justify-content: center; gap: 70px;
  }
  .card {
    position: relative; width: 460px; height: 460px;
    background: var(--card); border-radius: 34px; overflow: hidden;
    box-shadow: 0 18px 40px rgba(0,0,0,.5);
  }
  .edge-band { position: absolute; left: 0; right: 0; bottom: 0; height: 10px; display: flex; }
  .edge-band .blue { flex: 0 0 45%; background: var(--blue); }
  .edge-band .pink { flex: 1; background: var(--pink); }

  /* Front */
  .backdrop-shape {
    position: absolute; left: 60px; top: 70px; width: 340px; height: 300px;
    border-radius: 50%; background: radial-gradient(circle, var(--card-soft), transparent 70%);
  }
  .brand { position: absolute; right: 40px; top: 54px; text-align: right; }
  .brand-name { display: flex; align-items: center; justify-content: flex-end; gap: 10px;
    font-size: 38px; color: var(--blue); letter-spacing: .5px; }
  .brand-dot { width: 22px; height: 22px; border-radius: 50%; background: var(--blue); }
  .brand-slogan { font-size: 12px; color: var(--muted); letter-spacing: 6px; margin-top: 4px; }
  .person { position: absolute; right: 40px; top: 178px; text-align: right; }
  .person-name { font-size: 30px; color: var(--pink); font-weight: 400; }
  .person-role { font-size: 15px; color: var(--text); margin-top: 2px; }
  .contacts { position: absolute; right: 40px; top: 272px; text-align: right;
    font-size: 16px; color: var(--text); line-height: 1.65; }
  .contacts .label { color: var(--pink); margin-right: 6px; }
  .contacts .web { color: var(--blue); }

  /* Back */
  .tile-field { position: absolute; left: 30px; top: 150px; width: 400px; height: 260px;
    background: linear-gradient(135deg, #0f0f0f, #171717 50%, #0c0c0c); opacity: .8; border-radius: 8px; }
  .offer { position: absolute; right: 40px; top: 44px; text-align: right; }
  .offer-title { font-size: 32px; color: var(--blue); margin-bottom: 14px; }
  .offer-title .accent { color: var(--pink); }
  .offer-list { list-style: none; font-size: 15px; color: var(--text); line-height: 1.55; }
  .offer-list li { display: flex; justify-content: flex-end; align-items: center; gap: 8px; }
  .offer-list .bullet { width: 8px; height: 8px; border-radius: 50%; background: var(--blue); flex: none; }
  .offer-list .sub { color: var(--muted); }
  .social { position: absolute; left: 50px; bottom: 56px; display: flex; gap: 12px; }
  .social span { width: 26px; height: 26px; background: var(--pink); border-radius: 3px; }
</style>
</head>
<body>
  <section class="card card-front">
    <div class="backdrop-shape"></div>
    <div class="brand">
      <div class="brand-name"><span class="brand-dot"></span>RevelHubQZ</div>
      <div class="brand-slogan">discover nightlife</div>
    </div>
    <div class="person">
      <h1 class="person-name">Mara Quill</h1>
      <p class="person-role">Manager</p>
    </div>
    <div class="contacts">
      <p><span class="label">P:</span>+1 512-987-3304</p>
      <p><span class="label">E:</span>hello@revelhubqz.example</p>
      <p><span class="label">A:</span>Harbor Bay North Shore</p>
      <p class="web">www.revelhubqz.example</p>
    </div>
    <div class="edge-band"><span class="blue"></span><span class="pink"></span></div>
  </section>

  <section class="card card-back">
    <div class="tile-field" role="img" aria-label="Faint grid of dark tiles as background texture"></div>
    <div class="offer">
      <h2 class="offer-title">what <span class="accent">we</span> offer</h2>
      <ul class="offer-list">
        <li><span class="bullet"></span>Events</li>
        <li class="sub"><span class="bullet"></span>Search upcoming events</li>
        <li class="sub"><span class="bullet"></span>Submit events</li>
        <li><span class="bullet"></span>Party Image Gallery</li>
        <li class="sub"><span class="bullet"></span>View and download HQ party images</li>
        <li class="sub"><span class="bullet"></span>Sign up as a contributing event photographer</li>
        <li class="sub">and get paid!</li>
        <li><span class="bullet"></span>Tickets</li>
        <li class="sub"><span class="bullet"></span>Sell your event tickets online for free!</li>
        <li class="sub"><span class="bullet"></span>Direct pay</li>
        <li class="sub"><span class="bullet"></span>No ticket fee</li>
      </ul>
    </div>
    <div class="social" aria-label="Social links"><span></span><span></span><span></span></div>
    <div class="edge-band"><span class="blue"></span><span class="pink"></span></div>
  </section>
</body>
</html>
```